I'm looking for a book cover with the Main title:
Where the Lanterns Drift Beyond the Harbour Mist at Dusk

Subtitle: A Wanderer's Chronicle of Salt and Ember

Looking for a clean design that attracts people to the book.

Open to all styles of design (plain text, animated characters, scenery) as long as the text is in basic font and easy to read.

This is to be put somewhere under the titles
Written By: Bogumil Trenkaro

The back of the book will have:

"A physical, mental, emotional, and spiritual guide to fat loss. Going beyond calorie deficit diets and working out for hours a day in order to achieve results. It will help you get to the root cause of weight gain and give you the tools you need to take charge of your health and your life.

You will learn:
- The Best Foods to Eat for Fat Loss
- The Foods You Need to Avoid
- How to Heal Your Hormones
- Strategies to Overcome Emotional Eating
- Mindset and Motivation Tactics
- How to Meditate Without Losing Your Mind

I created this book to help those struggling with losing fat in a healthy, holistic, and sustainable way. It’s my sincere hope that this book gives you what you need in order to achieve your goals. "

Please place the photo somewhere on the back as well if it fits with the design.

Thank you for your time!

```html
<!DOCTYPE html>
<html lang="en">
<head>
<meta charset="utf-8">
<title>Where the Lanterns Drift Beyond the Harbour Mist at Dusk — Cover Spread</title>
<link rel="stylesheet" href="https://fonts.googleapis.com/css2?family=Bebas+Neue&family=Mulish:wght@400;500&family=Tinos:ital@1&display=swap">
<style>
  :root {
    --ink: #111111;
    --indigo: #5158a8;
    --rose: #ef5b7f;
    --peach: #f5b896;
    --paper: #ffffff;
    --trim: #8a8a8a;
  }
  * { box-sizing: border-box; margin: 0; padding: 0; }
  html, body {
    width: 1200px; height: 826px; overflow: hidden;
    background: var(--paper);
  }
  .spread { position: relative; width: 1200px; height: 826px; }

  .panel {
    position: absolute; top: 14px;
    width: 552px; height: 783px;
    border: 1px solid var(--trim);
    background: var(--paper);
    overflow: hidden;
  }
  .back  { left: 26px; }
  .front { left: 623px; }

  /* Back cover */
  .blurb {
    position: absolute; left: 45px; top: 61px; width: 462px;
    font-family: "Mulish", sans-serif; font-size: 13.3px; line-height: 26.4px;
    color: var(--ink);
  }
  .blurb-line {
    display: block; white-space: nowrap;
    text-align: justify; text-align-last: justify;
  }
  .blurb-line.last { text-align-last: left; }

  .learn {
    position: absolute; left: 99px; top: 188px;
    font-family: "Mulish", sans-serif; color: var(--ink);
  }
  .learn-heading { font-size: 16.5px; font-weight: 500; line-height: 20px; margin-bottom: 7.6px; }
  .learn-list { list-style: none; }
  .learn-list li {
    position: relative; padding-left: 24px;
    font-size: 16px; font-weight: 500; line-height: 20px; margin-bottom: 7.8px;
    white-space: nowrap;
  }
  .learn-list li::before {
    content: ""; position: absolute; left: 5px; top: 7px;
    width: 7px; height: 7px; border-radius: 50%; background: var(--indigo);
  }
  .learn-list li.two-line { line-height: 21.5px; }
  .kitchen-art {
    position: absolute; left: 47px; top: 412px; width: 458px; height: 152px;
    background: linear-gradient(90deg, #eef0fa 0%, #fbe6da 35%, #eef0fa 60%, #fbe6da 100%);
    border-radius: 6px;
  }
  .author-heading {
    position: absolute; left: 49px; top: 590px;
    font-family: "Mulish", sans-serif; font-size: 19px; font-weight: 500; line-height: 22px; color: var(--ink);
  }
  .author-photo {
    position: absolute; left: 51px; top: 630px;
    width: 108px; height: 108px; border-radius: 50%;
    background: radial-gradient(circle at 50% 45%, #8a6a55 0%, #5d6b4a 60%, #3b4a34 100%);
  }
  .author-note {
    position: absolute; left: 164px; top: 625px; width: 346px;
    font-family: "Tinos", serif; font-style: italic;
    font-size: 16.4px; line-height: 22px; color: var(--ink); text-align: center;
    white-space: nowrap;
  }

  /* Front cover */
  .subtitle {
    position: absolute; left: 0; right: 0; top: 50px;
    font-family: "Mulish", sans-serif; font-size: 22.5px; color: var(--ink);
    text-align: center;
  }
  .cover-art {
    position: absolute; left: -8px; top: 168px; width: 250px; height: 440px;
    background: linear-gradient(170deg, var(--peach) 0%, #f8cdb4 55%, var(--peach) 100%);
    border-radius: 40% 20% 45% 35% / 20% 30% 25% 35%;
    opacity: .95;
  }
  .title {
    position: absolute; right: 30px; top: 118px;
    font-family: "Bebas Neue", sans-serif; text-align: right;
    color: var(--indigo); line-height: .9;
  }
  .title-line { display: block; }
  .title-line.big    { font-size: 98px; }
  .title-line.medium { font-size: 80px; }
  .title-line.small  { font-size: 62px; }
  .accent { color: var(--rose); }
  .author {
    position: absolute; left: 0; right: 0; top: 698px;
    font-family: "Mulish", sans-serif; font-size: 44px; color: var(--ink);
    text-align: center; letter-spacing: -.5px;
  }
</style>
</head>
<body>
<main class="spread">
  <section class="panel back" aria-label="Back cover">
    <p class="blurb">
      <span class="blurb-line">A physical, mental, emotional, and spiritual guide to fat loss. Going</span>
      <span class="blurb-line">beyond calorie deficit diets and working out for hours a day in order to</span>
      <span class="blurb-line">achieve results. It will help you get to the root cause of weight gain and</span>
      <span class="blurb-line last">give you the tools you need to take charge of your health and your life.</span>
    </p>

    <div class="learn">
      <p class="learn-heading">You will learn:</p>
      <ul class="learn-list">
        <li>The Best Foods to Eat for Fat Loss</li>
        <li>The Foods You Need to Avoid</li>
        <li>How to Heal Your Hormones</li>
        <li>Strategies to Overcome Emotional Eating</li>
        <li>Mindset and Motivation Tactics</li>
        <li class="two-line">How to Meditate Without Losing<br>Your Mind</li>
      </ul>
    </div>

    <div class="kitchen-art" role="img" aria-label="Single-line drawing of kitchen items: pan, ladle, spatula, plate of fish with lemon slices, fork, pumpkin, eggplant, tomato and bottle with peach accents"></div>

    <h2 class="author-heading">About the Author</h2>
    <div class="author-photo" role="img" aria-label="Round portrait photo of the author outdoors"></div>
    <p class="author-note">I created this book to help those struggling with<br>losing fat in a healthy, holistic, and sustainable<br>way. It’s my sincere hope that this book gives<br>you what you need in order to achieve your goals.</p>
  </section>

  <section class="panel front" aria-label="Front cover">
    <p class="subtitle">A Wanderer's Chronicle of Salt and Ember</p>
    <div class="cover-art" role="img" aria-label="Line illustration of a figure's torso with a tape measure, in indigo lines over peach shapes"></div>
    <h1 class="title">
      <span class="title-line small accent">Where the</span>
      <span class="title-line big">Lanterns</span>
      <span class="title-line small accent">Drift Beyond</span>
      <span class="title-line medium">The Harbour</span>
      <span class="title-line big">Mist <span class="accent">at</span></span>
      <span class="title-line big">Dusk</span>
    </h1>
    <p class="author">Bogumil Trenkaro</p>
  </section>
</main>
</body>
</html>
```